Business card design needed

Want the logo on a medium blue background and a nice funky design. I have my own gym and run one on one personal training and nutrition sessions. want it to look lively.
Updates

Please note I requested my logo on a blue background 

PLEASE NOTE: I already have a logo. It is attached to the order!!

Target Market(s)

over 55s

Industry/Entity Type

Nutrition

Contact Information for Business Card

Front of card : Logo ( on blue background )
Corinne Dalby
Nutrition & Fitness Coach for Seniors
Private gym at : 17 Fennick Street, Brantwood, Perth, WA 6291
Mob : 0412736158
Email : corinnedalby@fernpost.example
"Fit for Life at Every Age"

Back of card
B.A. ( Soc.)
Dip. Ed. (Sec.)
Wellness Coach
Cert 4 Personal Trainer
Cert. Nutrition
MOVE ON Facilitator
Ageing Well Moving Freely Facilitator
Pilates Level 2

```html
<!DOCTYPE html>
<html lang="en">
<head>
<meta charset="utf-8">
<title>Silver Stride Nutrition &amp; Fitness – Business Card</title>
<link rel="stylesheet" href="https://fonts.googleapis.com/css2?family=PT+Sans:wght@400&family=Quicksand:wght@500&display=swap">
<style>
  :root {
    --stage: #000000;
    --card-edge: #d9e6f5;
    --text-white: #ffffff;
    --brand-gold: #f2d23c;
  }
  html, body {
    margin: 0;
    padding: 0;
    width: 1200px;
    height: 1000px;
    overflow: hidden;
    background: var(--stage);
  }
  .canvas {
    position: relative;
    width: 1200px;
    height: 1000px;
    background: var(--stage);
  }
  .card {
    position: absolute;
    width: 686px;
    height: 424px;
    overflow: hidden;
    border: 1px solid var(--card-edge);
    box-sizing: border-box;
    font-family: "PT Sans", sans-serif;
    color: var(--text-white);
  }
  .card--front { left: 126px; top: 60px; }
  .card--back  { left: 374px; top: 502px; width: 688px; }
  .card__backdrop {
    position: absolute;
    inset: 0;
    width: 100%;
    height: 100%;
  }
  .brand {
    position: absolute;
    display: flex;
    flex-direction: column;
    align-items: center;
    color: var(--brand-gold);
    font-family: "Quicksand", sans-serif;
    font-weight: 500;
    line-height: 1.1;
  }
  .brand__dot {
    border-radius: 50%;
    background: var(--brand-gold);
  }
  .card--front .brand {
    left: 80px;
    top: 170px;
    width: 250px;
    font-size: 32px;
  }
  .card--front .brand__dot { width: 30px; height: 30px; margin-bottom: 10px; }
  .card--front .brand__sub { font-size: 22px; margin-top: 6px; }
  .card--back .brand {
    left: 234px;
    top: 76px;
    width: 220px;
    font-size: 22px;
  }
  .card--back .brand__dot { width: 24px; height: 24px; margin-bottom: 10px; }
  .card--back .brand__sub { font-size: 16px; margin-top: 4px; }
  .contact {
    position: absolute;
    left: 336px;
    top: 122px;
    padding: 0 0 0 14px;
    border-left: 1.5px solid var(--text-white);
    font-size: 18px;
    line-height: 26px;
    margin: 0;
    list-style: none;
    white-space: nowrap;
  }
  .credentials {
    position: absolute;
    left: 0;
    right: 0;
    top: 240px;
    margin: 0;
    text-align: center;
    font-size: 18px;
    line-height: 26px;
  }
</style>
</head>
<body>
<main class="canvas">

  <svg width="0" height="0" style="position:absolute" aria-hidden="true">
    <defs>
      <linearGradient id="baseBlue" x1="0" y1="0" x2="1" y2="1">
        <stop offset="0" stop-color="#6fb0e6"/>
        <stop offset="0.45" stop-color="#3d78cf"/>
        <stop offset="1" stop-color="#1a2f88"/>
      </linearGradient>
      <radialGradient id="paleWash" cx="0.05" cy="0.35" r="0.55">
        <stop offset="0" stop-color="#e6f3fb" stop-opacity="0.9"/>
        <stop offset="1" stop-color="#e6f3fb" stop-opacity="0"/>
      </radialGradient>
      <linearGradient id="bandLight" x1="0" y1="1" x2="1" y2="0">
        <stop offset="0" stop-color="#bfe6fa" stop-opacity="0.95"/>
        <stop offset="1" stop-color="#3f8fe0" stop-opacity="0.4"/>
      </linearGradient>
      <linearGradient id="topSweep" x1="0" y1="0" x2="1" y2="0">
        <stop offset="0" stop-color="#a9d6f3" stop-opacity="0.8"/>
        <stop offset="1" stop-color="#5aa4e4" stop-opacity="0.3"/>
      </linearGradient>
    </defs>
  </svg>

  <section class="card card--front" aria-label="Business card front">
    <svg class="card__backdrop" viewBox="0 0 686 424" preserveAspectRatio="none" aria-hidden="true">
      <rect width="686" height="424" fill="url(#baseBlue)"/>
      <rect width="686" height="424" fill="url(#paleWash)"/>
      <path d="M0 0 H686 V40 C520 60 420 120 260 130 C160 136 60 110 0 90 Z" fill="url(#topSweep)" opacity="0.6"/>
      <path d="M0 250 C180 190 420 170 686 100 V150 C460 210 220 240 0 300 Z" fill="#2d56b8" opacity="0.45"/>
      <path d="M500 424 C590 360 650 290 686 220 V250 C660 320 600 380 540 424 Z" fill="url(#bandLight)"/>
      <path d="M600 424 C640 390 670 350 686 320 V350 C670 380 645 405 625 424 Z" fill="#a9dcf6" opacity="0.8"/>
      <path d="M430 424 C540 360 620 300 686 250 V230 C610 290 520 360 400 424 Z" fill="#6fb4ea" opacity="0.35"/>
    </svg>

    <div class="brand">
      <span class="brand__dot"></span>
      <span class="brand__name">Silver Stride</span>
      <span class="brand__sub">Nutrition &amp; Fitness</span>
    </div>

    <ul class="contact">
      <li>Corinne Dalby Nutrition &amp;</li>
      <li>Fitness Coach for Seniors</li>
      <li>Private gym at : 17 Fennick Street,</li>
      <li>Brantwood, Perth, WA 6291</li>
      <li>Mob : 0412736158</li>
      <li>Email : corinnedalby@fernpost.example</li>
      <li>"Fit for Life at Every Age"</li>
    </ul>
  </section>

  <section class="card card--back" aria-label="Business card back">
    <svg class="card__backdrop" viewBox="0 0 686 424" preserveAspectRatio="none" aria-hidden="true">
      <rect width="686" height="424" fill="url(#baseBlue)"/>
      <rect width="686" height="424" fill="url(#paleWash)"/>
      <path d="M0 0 H686 V40 C520 60 420 120 260 130 C160 136 60 110 0 90 Z" fill="url(#topSweep)" opacity="0.6"/>
      <path d="M0 250 C180 190 420 170 686 100 V150 C460 210 220 240 0 300 Z" fill="#2d56b8" opacity="0.45"/>
      <path d="M500 424 C590 360 650 290 686 220 V250 C660 320 600 380 540 424 Z" fill="url(#bandLight)"/>
      <path d="M600 424 C640 390 670 350 686 320 V350 C670 380 645 405 625 424 Z" fill="#a9dcf6" opacity="0.8"/>
      <path d="M430 424 C540 360 620 300 686 250 V230 C610 290 520 360 400 424 Z" fill="#6fb4ea" opacity="0.35"/>
    </svg>

    <div class="brand">
      <span class="brand__dot"></span>
      <span class="brand__name">Silver Stride</span>
      <span class="brand__sub">Nutrition &amp; Fitness</span>
    </div>

    <p class="credentials">
      B.A. (Psych.) Grad. Dip. (Hlth.)<br>
      Lifestyle Coach Cert 3 Fitness Instructor Cert.<br>
      Nutrition MOVE ON Facilitator Ageing Well Moving Freely<br>
      Facilitator Pilates Level 2
    </p>
  </section>

</main>
</body>
</html>
```